New business card design to go with our new logo

just want an eye-catching business card to go with our new logo. We are open to double sided or single sided. Just want it to have the following info on it. Whatever layout you think looks best.

First and Last Name
Title
Phone 801-555-0187
Address 312 W. Larkmoor Avenue Orem UT 84057
Email thecrew@meadowstailandkennel.example

Industry/Entity Type

Business

```html
<!DOCTYPE html>
<html lang="en">
<head>
<meta charset="utf-8">
<title>Meadows Tail &amp; Kennel — Business Card</title>
<link rel="stylesheet" href="https://fonts.googleapis.com/css2?family=Open+Sans:wght@400;600&display=swap">
<style>
  :root {
    --page-bg: #e8e6e3;
    --card-white: #f7f6f2;
    --brand-blue: #1f9ccc;
    --brand-blue-deep: #1386b3;
    --brand-orange: #ee8a3c;
    --text-light: #ffffff;
  }
  * { margin: 0; padding: 0; box-sizing: border-box; }
  html, body {
    width: 1200px; height: 1200px; overflow: hidden;
    background: var(--page-bg);
    font-family: "Open Sans", sans-serif;
  }
  .business-card {
    position: absolute; left: 75px; top: 300px;
    width: 1050px; height: 600px;
    background: var(--card-white);
    overflow: hidden;
    box-shadow: 0 14px 40px rgba(0,0,0,0.18);
  }
  .card-art { position: absolute; inset: 0; width: 100%; height: 100%; }
  .brand-name {
    position: absolute; left: 120px; top: 210px;
    display: flex; align-items: center; gap: 18px;
    color: var(--brand-orange); font-weight: 600;
  }
  .brand-mark {
    width: 46px; height: 46px; border-radius: 50%;
    background: var(--brand-orange); flex: none;
  }
  .brand-text { line-height: 1.05; }
  .brand-text .line-main { display: block; font-size: 58px; letter-spacing: 1px; }
  .brand-text .line-sub { display: block; font-size: 25px; letter-spacing: 3px; }
  .person {
    position: absolute; right: 130px; top: 80px; text-align: right;
    color: var(--brand-blue);
  }
  .person-name { font-size: 52px; font-weight: 600; letter-spacing: 0.5px; line-height: 1.1; }
  .person-title { font-size: 24px; font-weight: 400; }
  .contact-list {
    position: absolute; right: 40px; top: 330px; width: 640px;
    list-style: none; color: var(--text-light);
  }
  .contact-item {
    display: flex; justify-content: flex-end; align-items: center; gap: 16px;
    font-size: 26px; line-height: 1; margin-bottom: 20px;
  }
  .contact-item svg { width: 30px; height: 30px; flex: none; }
  .contact-divider {
    height: 1px; background: rgba(255,255,255,0.7);
    margin: 4px 0 20px 40px;
  }
</style>
</head>
<body>
  <article class="business-card">
    <svg class="card-art" viewBox="0 0 1050 600" aria-hidden="true">
      <path d="M0,372 C300,405 480,360 640,262 C780,178 900,148 1050,160 L1050,600 L0,600 Z" fill="var(--brand-blue)"/>
      <path d="M0,372 C300,405 480,360 640,262 C780,178 900,148 1050,160" fill="none" stroke="var(--brand-blue-deep)" stroke-width="4"/>
      <path d="M0,318 C160,342 360,330 530,272 C370,345 160,375 0,368 Z" fill="var(--brand-orange)"/>
      <g fill="var(--brand-blue)">
        <circle cx="545" cy="262" r="14"/>
        <circle cx="582" cy="246" r="14" opacity="0.9"/>
        <circle cx="622" cy="228" r="14" opacity="0.75"/>
        <circle cx="662" cy="210" r="14" opacity="0.6"/>
        <circle cx="702" cy="190" r="14" opacity="0.45"/>
        <circle cx="742" cy="172" r="14" opacity="0.3"/>
        <circle cx="782" cy="156" r="14" opacity="0.15"/>
      </g>
    </svg>

    <div class="brand-name">
      <span class="brand-mark"></span>
      <span class="brand-text">
        <span class="line-main">MEADOWS</span>
        <span class="line-sub">TAIL &amp; KENNEL</span>
      </span>
    </div>

    <header class="person">
      <h1 class="person-name">JOHN DOE</h1>
      <p class="person-title">Director</p>
    </header>

    <ul class="contact-list">
      <li class="contact-item">801-555-0187
        <svg viewBox="0 0 24 24" fill="#fff"><path d="M3 9c0-3 4-5 9-5s9 2 9 5v1h-4l-1-2H8L7 10H3z"/><path d="M6 12l2-3h8l2 3v7H6z"/><circle cx="12" cy="15" r="2" fill="var(--brand-blue)"/></svg>
      </li>
      <li class="contact-item">thecrew@meadowstailandkennel.example
        <svg viewBox="0 0 24 24"><rect x="2" y="5" width="20" height="14" fill="#fff"/><path d="M2 5l10 8 10-8M2 19l8-7M22 19l-8-7" fill="none" stroke="var(--brand-blue)" stroke-width="1.5"/></svg>
      </li>
      <li class="contact-divider"></li>
      <li class="contact-item">312 W. Larkmoor Avenue Orem UT 84057
        <svg viewBox="0 0 24 24" fill="#fff"><path d="M12 2a7 7 0 0 0-7 7c0 5 7 13 7 13s7-8 7-13a7 7 0 0 0-7-7z"/><circle cx="12" cy="9" r="3" fill="var(--brand-blue)"/></svg>
      </li>
    </ul>
  </article>
</body>
</html>
```